Business Cards

We are an innovating group of real estate investors who buy beat up house's, fix them up, and resell them. We are in need of a business card that is catchy and stands out. We want it to say something like " We buy house's cash fast" Call us first

Industry/Entity Type

Business

Requirements
Must have
• Our logo which is updated

```html
<!DOCTYPE html>
<html lang="en">
<head>
<meta charset="utf-8">
<title>Fixwell Homes — Business Cards</title>
<link rel="stylesheet" href="https://fonts.googleapis.com/css2?family=Arimo:wght@400;700&display=swap">
<style>
  :root {
    --canvas-bg: #e9e6e1;
    --card-white: #ffffff;
    --brand-purple: #a0149f;
    --brand-green: #4e8a19;
    --text-dark: #1d1d1d;
    --text-light: #ffffff;
  }
  * { margin: 0; padding: 0; box-sizing: border-box; }
  html, body { width: 1200px; height: 800px; overflow: hidden; }
  body {
    background: var(--canvas-bg);
    font-family: "Arimo", Arial, sans-serif;
    position: relative;
  }
  .card {
    position: absolute;
    width: 600px;
    height: 340px;
    background: var(--card-white);
    border-radius: 28px;
    overflow: hidden;
    box-shadow: 0 6px 18px rgba(0,0,0,0.18);
  }
  .card--front { left: 60px; top: 60px; }
  .card--back { left: 540px; top: 400px; }

  .rule-purple {
    position: absolute; left: 0; right: 0;
    height: 7px; background: var(--brand-purple);
  }
  .band-green {
    position: absolute; left: 0; right: 0; bottom: 0;
    background: var(--brand-green);
    color: var(--text-light);
    font-weight: 700;
    display: flex; align-items: center; justify-content: center;
  }
  .card--front .rule-purple { top: 266px; }
  .card--front .band-green { height: 60px; font-size: 19px; letter-spacing: 2.4px; }
  .card--back .rule-purple { top: 248px; }
  .card--back .band-green { height: 78px; font-size: 23px; letter-spacing: 0.5px; }

  .brand-name {
    position: absolute;
    display: flex; align-items: center; gap: 10px;
    color: var(--brand-purple);
    font-weight: 700;
    white-space: nowrap;
  }
  .brand-name__square {
    width: 18px; height: 18px; background: var(--brand-green);
  }
  .card--front .brand-name { left: 0; right: 0; justify-content: center; top: 112px; font-size: 34px; }
  .card--back .brand-name { left: 150px; top: 40px; font-size: 24px; }

  .holder-name {
    position: absolute; right: 330px; top: 158px;
    color: var(--brand-purple);
    font-weight: 700; font-size: 24px;
    white-space: nowrap;
  }
  .divider {
    position: absolute; left: 290px; top: 110px;
    width: 4px; height: 114px; background: var(--brand-green);
  }
  .contact-list {
    position: absolute; left: 312px; top: 106px;
    list-style: none;
    color: var(--text-dark);
    font-size: 17px; line-height: 1.2;
  }
  .contact-list li { display: flex; align-items: flex-start; gap: 8px; margin-bottom: 6px; }
  .contact-list svg { flex: none; width: 16px; height: 16px; margin-top: 2px; fill: var(--brand-purple); }
</style>
</head>
<body>
  <section class="card card--front" aria-label="Card front">
    <div class="brand-name"><span class="brand-name__square"></span>Fixwell Homes</div>
    <div class="rule-purple"></div>
    <div class="band-green">WE BUY HOUSE'S CASH FAST</div>
  </section>

  <section class="card card--back" aria-label="Card back">
    <div class="brand-name"><span class="brand-name__square"></span>Fixwell Homes</div>
    <div class="holder-name">Your Name</div>
    <div class="divider"></div>
    <ul class="contact-list">
      <li>
        <svg viewBox="0 0 16 16" aria-hidden="true"><path d="M3.2 1.5l2.4 0 1.1 3.2-1.6 1.2c.8 1.8 2.2 3.2 4 4l1.2-1.6 3.2 1.1v2.4c0 1-1 1.9-2 1.7C6.4 12.8 3.2 9.6 2.5 4.5 2.3 3.5 2.2 1.5 3.2 1.5z"/></svg>
        <span>999-999-9999</span>
      </li>
      <li>
        <svg viewBox="0 0 16 16" aria-hidden="true"><path d="M1 4h14v9H1z M2.2 5.2l5.8 4.3 5.8-4.3" fill="none" stroke="#a0149f" stroke-width="1.8"/></svg>
        <span>email.id@mail.com</span>
      </li>
      <li>
        <svg viewBox="0 0 16 16" aria-hidden="true"><path d="M8 1.5l7 6.3h-2.2V14H9.8v-4H6.2v4H3.2V7.8H1z"/></svg>
        <span>Address line 1, xxxxxxxx<br>Address line 2</span>
      </li>
    </ul>
    <div class="rule-purple"></div>
    <div class="band-green">www.websitename.com</div>
  </section>
</body>
</html>
```